Luminously Grounded Vitality

We want to design a business card that is modern and appealing for an innovative psychedelic telemedicine company that provides at-home ketamine-assisted therapy along with wellness, longevity, and anti-aging medicines. We want to use our deep purple and white plus other colors you can find on our website. We don't have any strict brand guidelines yet so feel free to get creative. We want a very professional, but technology first modern design that will instill trust, peace, calm, but also be attractive to investors in the healthcare and SaaS space.

```html
<!DOCTYPE html>
<html lang="en">
<head>
<meta charset="utf-8">
<title>Luminously Grounded Vitality – Business Card</title>
<link rel="stylesheet" href="https://fonts.googleapis.com/css2?family=Lato:wght@400;700&display=swap">
<style>
  :root {
    --stage: #2a2a2c;
    --brand-purple: #7d67a8;
    --deep-purple: #6a55a0;
    --orchid: #b066a3;
    --card-white: #f7f7f8;
    --ink: #333336;
    --on-purple: #ffffff;
  }
  * { box-sizing: border-box; margin: 0; padding: 0; }
  html, body {
    width: 1200px; height: 1156px; overflow: hidden;
    background: var(--stage);
    font-family: "Lato", sans-serif;
  }
  .canvas {
    width: 1200px; height: 1156px;
    display: flex; flex-direction: column; align-items: center; justify-content: center;
    gap: 66px;
  }
  .card {
    width: 840px; height: 480px; position: relative; overflow: hidden;
    box-shadow: 0 10px 30px rgba(0,0,0,.45);
  }
  /* Back */
  .card-back {
    background: var(--brand-purple);
    display: flex; align-items: center; justify-content: center;
  }
  .brand {
    display: flex; align-items: center; gap: 18px;
  }
  .brand-dot { width: 34px; height: 34px; border-radius: 50%; flex: none; }
  .brand-name { font-size: 40px; font-weight: 400; letter-spacing: .5px; }
  .card-back .brand-dot { background: var(--on-purple); }
  .card-back .brand-name { color: var(--on-purple); }

  /* Front */
  .card-front {
    background: var(--card-white);
    display: grid; grid-template-columns: 1fr 1fr;
  }
  .front-brand {
    display: flex; align-items: center; justify-content: center; padding-left: 40px;
  }
  .front-brand .brand { flex-direction: row; gap: 14px; }
  .front-brand .brand-dot { background: var(--deep-purple); width: 26px; height: 26px; }
  .front-brand .brand-name {
    color: var(--orchid); font-size: 31px; line-height: 1.15; max-width: 300px;
  }
  .contact-block {
    padding: 150px 0 0 20px;
  }
  .person-name {
    color: var(--deep-purple); font-size: 34px; font-weight: 700; letter-spacing: .5px;
    text-transform: uppercase; line-height: 1;
  }
  .person-title { color: var(--ink); font-size: 17px; margin-top: 6px; }
  .divider {
    height: 2px; background: var(--deep-purple); margin: 12px 0 18px -10px; width: calc(100% + 10px);
  }
  .contact-list { list-style: none; display: flex; flex-direction: column; gap: 9px; }
  .contact-item {
    display: flex; align-items: flex-start; gap: 12px;
    color: var(--ink); font-size: 18px; line-height: 1.22;
  }
  .contact-icon { width: 16px; height: 16px; flex: none; margin-top: 3px; }
  .contact-icon path, .contact-icon circle, .contact-icon rect {
    fill: none; stroke: var(--orchid); stroke-width: 1.6; stroke-linecap: round; stroke-linejoin: round;
  }
</style>
</head>
<body>
<main class="canvas">
  <section class="card card-back" aria-label="Card back">
    <div class="brand">
      <span class="brand-dot"></span>
      <span class="brand-name">Luminously Grounded Vitality</span>
    </div>
  </section>

  <section class="card card-front" aria-label="Card front">
    <div class="front-brand">
      <div class="brand">
        <span class="brand-dot"></span>
        <span class="brand-name">Luminously Grounded Vitality</span>
      </div>
    </div>
    <div class="contact-block">
      <h1 class="person-name">Daniel Reyes</h1>
      <p class="person-title">Manager</p>
      <div class="divider"></div>
      <ul class="contact-list">
        <li class="contact-item">
          <svg class="contact-icon" viewBox="0 0 16 16"><path d="M8 15s5-5 5-8.5A5 5 0 0 0 3 6.5C3 10 8 15 8 15z"/><circle cx="8" cy="6.5" r="1.8"/></svg>
          <span>245 Alder Avenue, Suite 900<br>Boulder, CO, United States, 80302</span>
        </li>
        <li class="contact-item">
          <svg class="contact-icon" viewBox="0 0 16 16"><path d="M4 1.5l2 3-1.3 1.5a8 8 0 0 0 5.3 5.3L11.5 10l3 2-1 2.5C7 14.5 1.5 9 1.5 2.5z"/></svg>
          <span>+1 833-555-0192</span>
        </li>
        <li class="contact-item">
          <svg class="contact-icon" viewBox="0 0 16 16"><rect x="1.5" y="3.5" width="13" height="9" rx="1"/><path d="M1.5 4l6.5 5 6.5-5"/></svg>
          <span>hello@luminouslyvitality.com</span>
        </li>
        <li class="contact-item">
          <svg class="contact-icon" viewBox="0 0 16 16"><circle cx="8" cy="8" r="6.5"/><path d="M1.5 8h13M8 1.5c2 2 2 11 0 13M8 1.5c-2 2-2 11 0 13"/></svg>
          <span>www.luminouslyvitality.com</span>
        </li>
      </ul>
    </div>
  </section>
</main>
</body>
</html>
```